Ecommerce website Home Page Design that is clean and elegant

Design a Home page for an ecommerce website. This website products and offerings will be very similar to :

breezyharborcharms.com
maplecrestbazaar.com

Target Market(s)

Consumer and small shops who can order online.

Industry/Entity Type

Retail

Number of Pages Required

1 page

Colors

Designer to choose colors to be used in the design.

Requirements
Must have
• Exact competition with similar products:
• breezyharborcharms.com
• http://www.maplecrestbazaar.com/
• Home page with featured image banner
• List of items on sale or category based items list
• atleast three banners for sale or shipping related offers.
Nice to have
• The logo has very light colors and products will have lots of colors as you can see on competition sites. So the design must consider this so that logo also stands out somewhat for branding purpose.
Should not have
• Design should not have black background

```html
<!DOCTYPE html>
<html lang="en">
<head>
<meta charset="utf-8">
<title>Brightwick – Party &amp; Novelty Supplies</title>
<link href="https://fonts.googleapis.com/css2?family=Raleway:wght@400;500;600;700;800&display=swap" rel="stylesheet">
<style>
:root{
  --teal:#7fc0c8;
  --teal-deep:#5fb0ba;
  --orange:#e8a04a;
  --pink:#f48ca0;
  --purple:#a98bc4;
  --ink:#2f2f2f;
  --muted:#777;
  --white:#ffffff;
  --line:#d6d6d6;
  --page:#ffffff;
}
*{box-sizing:border-box;margin:0;padding:0}
html,body{width:1200px;height:2546px;overflow:hidden;background:var(--page)}
body{font-family:"Raleway",sans-serif;color:var(--ink);position:relative}
.abs{position:absolute}

/* header */
.brand{left:150px;top:16px;font-size:27px;font-weight:700;line-height:32px;color:var(--teal);white-space:nowrap}
.social{display:flex;gap:8px}
.social span{width:20px;height:20px;border-radius:50%;display:block}
.header-social{left:322px;top:22px}
.c1{background:#8aa3c9}.c2{background:#3d8ec4}.c3{background:#8ccbe8}.c4{background:#e49a8f}
.search{left:777px;top:20px;width:170px;height:24px;border:1px solid #e2e2e2;border-radius:12px;font-size:9px;color:#aaa;padding:6px 12px;background:#fafafa}
.search::after{content:"";position:absolute;right:0;top:-1px;width:36px;height:24px;border-radius:12px;background:#ececec}
.contact-btn{left:962px;top:18px;width:88px;height:26px;border:1.5px solid var(--orange);border-radius:13px;color:var(--orange);font-size:12px;font-weight:700;text-align:center;line-height:23px}
.nav{left:312px;top:65px;display:flex;gap:21px;font-size:12.5px;font-weight:700}
.nav .active{color:var(--orange)}

/* hero */
.hero{left:149px;top:105px;width:900px;height:411px;background:linear-gradient(135deg,#8cc6cc,#6fb4bd 55%,#86c3c9);text-align:center;color:var(--white)}
.hero h1{position:absolute;left:0;right:0;top:115px;font-size:62px;font-weight:800;line-height:62px}
.btn-orange{position:absolute;background:var(--orange);color:var(--white);font-size:11.5px;font-weight:700;border-radius:14px;text-align:center}
.hero .btn-orange{left:376px;top:262px;width:150px;height:26px;line-height:26px}

/* promo tiles */
.new-products{left:178px;top:572px}
.new-products h2{font-size:28px;font-weight:600;color:var(--teal);line-height:28px}
.new-products p{font-size:11px;margin-top:8px;line-height:15px}
.dots{display:flex;gap:5px}
.dots span{width:13px;height:13px;border-radius:50%;background:#f2d9b2}
.dots .on{background:var(--orange)}
.new-dots{left:180px;top:720px}
.new-photo{left:322px;top:548px;width:262px;height:214px;background:radial-gradient(circle at 50% 45%,#5de07a,#e07bd3 30%,#2a2a2a 70%,#0c0c0c)}
.sale-tile{left:614px;top:546px;width:435px;height:462px;background:linear-gradient(160deg,#b39bcc,#9e84bd);color:var(--white);font-size:28px;font-weight:700;display:flex;align-items:center;justify-content:center}
.about{left:149px;top:793px;width:435px;height:215px;background:var(--pink);color:var(--white);text-align:center;padding:50px 62px 0}
.about h2{font-size:28px;font-weight:700;margin-bottom:10px}
.about p{font-size:11px;line-height:17.5px}

/* categories */
.cat{width:200px;text-align:center;color:var(--orange);font-size:18px;font-weight:700}
.cat svg{display:block;margin:0 auto 20px;stroke:#555;stroke-width:2;fill:none;stroke-linejoin:round;stroke-linecap:round}

/* gallery */
.gallery{left:149px;top:1431px;width:900px;height:456px;background:linear-gradient(120deg,#8dc5cc,#9ccdd2 50%,#8bc2c9)}
.gallery h2{position:absolute;left:0;right:0;top:52px;text-align:center;color:var(--white);font-size:28px;font-weight:700}
.thumb{position:absolute;top:115px;width:198px;height:199px;background:var(--white)}
.thumb i{position:absolute;inset:28px;border-radius:40%;display:block}
.gallery-dots{left:423px;top:346px}
.gallery-dots span{width:12px;height:12px;background:rgba(255,255,255,.55)}
.gallery-dots .on{background:var(--white)}
.view-all{position:absolute;left:0;right:0;top:386px;text-align:center;font-size:10px;color:var(--orange)}

/* contact */
.contact{left:149px;top:1918px;width:900px;height:290px;background:linear-gradient(135deg,#6e6a6a,#8a8585 50%,#5f5c5c)}
.contact h2{position:absolute;left:0;right:0;top:52px;text-align:center;color:var(--white);font-size:28px;font-weight:700}
.field{position:absolute;background:var(--white);border-radius:10px;font-size:10px;color:#bbb;padding:5px 14px}
.submit{position:absolute;left:333px;top:207px;width:236px;height:24px;border:1.5px solid var(--orange);border-radius:12px;color:var(--orange);font-size:11px;font-weight:700;text-align:center;line-height:21px}

/* footer */
.footer{left:0;top:2238px;width:1200px;height:308px;background:var(--teal);color:var(--white)}
.footer h3{position:absolute;top:56px;font-size:17px;font-weight:700}
.links{position:absolute;top:96px;list-style:none;font-size:12px;line-height:24px}
.contact-list{position:absolute;left:530px;top:100px;font-size:12px;line-height:22px}
.contact-list div{display:flex;gap:12px;margin-bottom:18px}
.contact-list svg{stroke:var(--white);fill:none;stroke-width:1.5;flex:none;margin-top:4px}
.footer-social{position:absolute;left:726px;top:106px}
.footer-social span{width:18px;height:18px}
.copyright{position:absolute;left:0;right:0;top:282px;text-align:center;font-size:9px}
</style>
</head>
<body>

<header>
  <div class="abs brand">Brightwick</div>
  <div class="abs social header-social"><span class="c1"></span><span class="c2"></span><span class="c3"></span><span class="c4"></span></div>
  <div class="abs search">Enter key words here</div>
  <div class="abs contact-btn">Contact</div>
  <nav class="abs nav">
    <span>Party Supplies</span><span>Occasions &amp; Events</span><span>Toys &amp; Games</span><span class="active">Crafts</span><span>Weddings</span><span>Holidays</span><span>Sale</span>
  </nav>
</header>

<section class="abs hero" role="img" aria-label="Photo of friends celebrating under falling confetti, tinted teal">
  <h1>Lorem ipsum dolor<br>sit amet</h1>
  <span class="btn-orange">View Our Products</span>
</section>

<div class="abs new-products">
  <h2>New<br>Products</h2>
  <p>Check out our latest<br>new products</p>
</div>
<div class="abs dots new-dots"><span class="on"></span><span></span><span></span><span></span></div>
<div class="abs new-photo" role="img" aria-label="Photo of colourful glow sticks in a glass on a dark background"></div>
<div class="abs sale-tile" role="img" aria-label="Photo of children at a birthday party, tinted purple">Items On Sale</div>
<section class="abs about">
  <h2>About Us</h2>
  <p>Nulla eu mauris et orci scelerisque aliquam in quis mi. Proin augue enim, rutrum ultricies leo et, sollicitudin pharetra odio. Praesent tristique accumsan est, nec bibendum felis tristique in.</p>
</section>

<!-- category grid -->
<div class="abs cat" style="left:295px;top:1068px">
  <svg width="60" height="76" viewBox="0 0 60 76"><path d="M20 8 L42 16 L20 26 L42 36 L20 46 L42 56 L20 66"/><path d="M8 10l4 4m0-4l-4 4M50 40l4 4m0-4l-4 4M10 58l3 3m0-3l-3 3"/></svg>
  Party Supplies</div>
<div class="abs cat" style="left:501px;top:1068px">
  <svg width="76" height="76" viewBox="0 0 76 76"><rect x="4" y="10" width="68" height="62" rx="4"/><path d="M4 24h68M20 4v12M56 4v12"/><path d="M38 32l5 10 11 1-8 7 3 11-11-6-11 6 3-11-8-7 11-1z"/></svg>
  Occasions &amp; Events</div>
<div class="abs cat" style="left:703px;top:1068px">
  <svg width="80" height="76" viewBox="0 0 80 76"><path d="M14 22h52c8 0 12 10 12 24s-6 20-12 16l-10-10H24L14 62c-6 4-12-2-12-16s4-24 12-24z"/><path d="M20 34v12M14 40h12"/><circle cx="56" cy="36" r="3"/><circle cx="62" cy="42" r="3"/><circle cx="50" cy="42" r="3"/></svg>
  Toys &amp; Games</div>
<div class="abs cat" style="left:295px;top:1248px">
  <svg width="70" height="76" viewBox="0 0 70 76"><path d="M14 10h12v22h38v26H14z"/><path d="M14 58v14M26 58v14M52 58v14M64 58v14M4 16h10"/><path d="M34 32v26M44 32v26M54 32v26"/></svg>
  Crafts</div>
<div class="abs cat" style="left:501px;top:1248px">
  <svg width="70" height="76" viewBox="0 0 70 76"><path d="M35 14c-13 0-18 12-18 26v14l-8 8h52l-8-8V40c0-14-5-26-18-26z"/><path d="M29 62a6 6 0 0012 0"/><path d="M35 14c-6-8-18-10-18-2s12 2 18 2c6 0 18 6 18-2s-12-6-18 2z"/></svg>
  Weddings</div>
<div class="abs cat" style="left:703px;top:1248px">
  <svg width="70" height="76" viewBox="0 0 70 76"><circle cx="35" cy="46" r="24"/><rect x="29" y="14" width="12" height="8"/><path d="M35 6v8M13 40h44M11 52h48"/></svg>
  Holidays</div>

<section class="abs gallery" role="img" aria-label="Photo of balloons against a white brick wall, tinted teal">
  <h2>View Our Gallery</h2>
  <div class="thumb" style="left:31px" role="img" aria-label="Photo of decorated masquerade masks"><i style="background:linear-gradient(120deg,#e9e1d0,#c9b48a 50%,#3f8a8c)"></i></div>
  <div class="thumb" style="left:245px" role="img" aria-label="Photo of patterned Halloween stockings"><i style="background:linear-gradient(120deg,#f1dede,#2d2d2d 60%,#1b1b1b)"></i></div>
  <div class="thumb" style="left:459px" role="img" aria-label="Photo of tinsel party wreaths"><i style="background:radial-gradient(circle,#fff 28%,#1e6b3a 30%,#3e2b6b 70%,#fff 72%)"></i></div>
  <div class="thumb" style="left:672px" role="img" aria-label="Photo of costume ear headbands and bow ties"><i style="background:linear-gradient(135deg,#f3f3f3,#d13b3b 50%,#f0c6d0)"></i></div>
  <div class="abs dots gallery-dots"><span class="on"></span><span></span><span></span></div>
  <div class="view-all">View All</div>
</section>

<section class="abs contact" role="img" aria-label="Photo of coloured markers and paint pots on paper, darkened">
  <h2>Contact Us</h2>
  <div class="field" style="left:177px;top:110px;width:236px;height:25px">Name</div>
  <div class="field" style="left:177px;top:151px;width:236px;height:24px">Email</div>
  <div class="field" style="left:428px;top:110px;width:297px;height:66px">Message</div>
  <div class="submit">Submit</div>
</section>

<footer class="abs footer">
  <h3 style="left:329px">Quick Links</h3>
  <ul class="links" style="left:329px">
    <li>Party Supplies</li><li>Occasions &amp; Events</li><li>Toys &amp; Games</li><li>Crafts</li><li>Weddings</li><li>Holidays</li><li>Sale</li>
  </ul>
  <h3 style="left:530px">Contact</h3>
  <div class="contact-list">
    <div><svg width="14" height="16" viewBox="0 0 14 16"><path d="M7 15s5-5 5-9A5 5 0 002 6c0 4 5 9 5 9z"/><circle cx="7" cy="6" r="1.8"/></svg><span>27 Lantern Row<br>Fairhaven, FL 30000</span></div>
    <div><svg width="14" height="14" viewBox="0 0 14 14"><path d="M3 1l3 3-2 2c1 2 2 3 4 4l2-2 3 3-2 2C6 13 1 8 1 3z"/></svg><span>555-014-2290</span></div>
    <div><svg width="14" height="12" viewBox="0 0 14 12"><rect x="1" y="1" width="12" height="10"/><path d="M1 1l6 5 6-5"/></svg><span>hello@brightwick.example</span></div>
  </div>
  <h3 style="left:726px">Keep Connected</h3>
  <div class="social footer-social"><span class="c1"></span><span class="c2"></span><span class="c3"></span><span class="c4"></span></div>
  <div class="copyright">© 2017 Brightwick All Rights Reserved</div>
</footer>

</body>
</html>
```